Tarvoe Aviation Consultants Business card

I need a business card design for a new aviation company called Tarvoe Aviation Consultants. Our focus is on large airplane end-of-life solutions. This is typically where an airline retires an aircraft and we would oversee the dismantling of the aircraft into the valuable components and parts. The removed parts are then overhauled and reintroduced into the market place.
'Tarvoe' means 'island in the clouds'. I envision an airplane flying into the sunset as it's days are numbered. I am also very keen on our Florida island vibe.
Industry/Entity Type
Aviation
Contact Information for Business Card
Tarvoe Aviation Consultants
End of Life Specialists
Dean Kross - President
418 SW 27th Ave
Fort Lauderdale, FL 33894
+1 954 555-0173
Logo Text
Requirements
Must have
- airplane
Nice to have
- sunset
- somewhere on the card it would be the definition of 'Tarvoe' - island in the clouds

```html
<!DOCTYPE html>
<html lang="en">
<head>
<meta charset="utf-8">
<title>Tarvoe Aviation Consultants – Business Card Variations</title>
<link rel="stylesheet" href="https://fonts.googleapis.com/css2?family=Arimo:wght@400;700&display=swap">
<style>
  :root {
    --stage: #8e8c82;
    --ink: #141414;
    --navy: #0b1c26;
    --paper: #eef4f4;
    --amber: #f5a623;
    --sunset-gold: #f4b148;
    --sunset-orange: #e07a1f;
    --sunset-brown: #7a4a22;
    --lagoon-light: #a6d5cc;
    --lagoon-mid: #4f8e92;
    --lagoon-deep: #1d4c5a;
    --dusk-light: #3a5d6a;
    --dusk-deep: #10252f;
    --coral-light: #f5b28e;
    --coral-mid: #e07d62;
    --coral-deep: #5e3a36;
  }
  html, body {
    margin: 0;
    padding: 0;
    width: 1200px;
    height: 1077px;
    overflow: hidden;
    background: var(--stage);
    font-family: "Arimo", Arial, sans-serif;
  }
  .sheet {
    position: relative;
    width: 1200px;
    height: 1077px;
  }
  .card {
    position: absolute;
    width: 406px;
    height: 250px;
    overflow: hidden;
  }
  .card--sunrise { left: 177px; top: 265px; }
  .card--lagoon  { left: 616px; top: 265px; }
  .card--dusk    { left: 177px; top: 566px; }
  .card--coral   { left: 616px; top: 566px; }

  .card__scene {
    position: absolute;
    inset: 0;
  }
  .card--sunrise .card__scene {
    background:
      linear-gradient(90deg, rgba(90,55,25,.75) 0%, rgba(90,55,25,0) 40%),
      linear-gradient(180deg, var(--sunset-gold) 0%, #f1952e 55%, var(--sunset-orange) 75%, #b8601e 100%);
  }
  .card--lagoon .card__scene {
    background:
      linear-gradient(90deg, rgba(20,55,65,.8) 0%, rgba(20,55,65,0) 40%),
      radial-gradient(ellipse at 55% 55%, var(--lagoon-light) 0%, var(--lagoon-mid) 55%, var(--lagoon-deep) 100%);
  }
  .card--dusk .card__scene {
    background:
      linear-gradient(90deg, rgba(10,28,36,.8) 0%, rgba(10,28,36,0) 40%),
      linear-gradient(180deg, var(--dusk-light) 0%, #2a4753 55%, var(--dusk-deep) 100%);
  }
  .card--coral .card__scene {
    background:
      linear-gradient(90deg, rgba(70,40,38,.8) 0%, rgba(70,40,38,0) 40%),
      radial-gradient(ellipse at 60% 65%, #f8c89a 0%, var(--coral-light) 25%, var(--coral-mid) 60%, var(--coral-deep) 100%);
  }

  .card__name {
    position: absolute;
    margin: 0;
    font-size: 15px;
    line-height: 17px;
    font-weight: 700;
  }
  .card__title {
    position: absolute;
    margin: 0;
    font-size: 11.5px;
    line-height: 14px;
    font-weight: 400;
  }
  .card__details {
    position: absolute;
    margin: 0;
    font-size: 11.5px;
    line-height: 14.6px;
    font-weight: 400;
    font-style: normal;
  }
  .card__bar {
    position: absolute;
    left: 224px;
    right: 0;
    top: 127px;
    height: 18px;
  }
  .card__rule {
    position: absolute;
    left: 244px;
    width: 142px;
    top: 141px;
    height: 2px;
    background: var(--navy);
  }

  /* left-aligned layouts */
  .card--sunrise .card__name,
  .card--dusk .card__name   { left: 224px; top: 90px; }
  .card--sunrise .card__title,
  .card--dusk .card__title  { left: 224px; top: 107px; }
  .card--sunrise .card__details,
  .card--dusk .card__details { left: 224px; top: 147px; }

  /* right-aligned layouts */
  .card--lagoon .card__name    { right: 20px; top: 101px; text-align: right; }
  .card--lagoon .card__title   { right: 20px; top: 119px; text-align: right; }
  .card--lagoon .card__details { right: 20px; top: 147px; text-align: right; }
  .card--coral .card__name     { right: 33px; top: 21px; text-align: right; }
  .card--coral .card__title    { right: 33px; top: 39px; text-align: right; }
  .card--coral .card__details  { right: 33px; top: 147px; text-align: right; }

  /* colourways */
  .card--sunrise .card__name { color: var(--ink); }
  .card--sunrise .card__title,
  .card--sunrise .card__details { color: var(--ink); }
  .card--sunrise .card__bar { background: var(--navy); }

  .card--lagoon .card__name { color: var(--navy); }
  .card--lagoon .card__title,
  .card--lagoon .card__details { color: var(--paper); }

  .card--dusk .card__name { color: var(--amber); }
  .card--dusk .card__title,
  .card--dusk .card__details { color: var(--paper); }
  .card--dusk .card__bar { background: var(--amber); }

  .card--coral .card__name { color: var(--navy); }
  .card--coral .card__title,
  .card--coral .card__details { color: var(--navy); }
</style>
</head>
<body>
<main class="sheet">

  <article class="card card--sunrise">
    <div class="card__scene" role="img" aria-label="Photograph of an airliner flying over a tropical shoreline with palm trees at a golden sunset"></div>
    <h2 class="card__name">employee name</h2>
    <p class="card__title">employee title</p>
    <div class="card__bar"></div>
    <address class="card__details">Tarvoe Aviation Consultants<br>End of Life Specialists<br>Dean Kross - President<br>418 SW 27th Ave<br>Fort Lauderdale, FL 33894<br>+1 954 555-0173</address>
  </article>

  <article class="card card--lagoon">
    <div class="card__scene" role="img" aria-label="Photograph of an airliner flying over a tropical shoreline with palm trees in teal evening light"></div>
    <h2 class="card__name">employee name</h2>
    <p class="card__title">employee title</p>
    <div class="card__rule"></div>
    <address class="card__details">Tarvoe Aviation Consultants<br>End of Life Specialists<br>Dean Kross - President<br>418 SW 27th Ave<br>Fort Lauderdale, FL 33894<br>+1 954 555-0173</address>
  </article>

  <article class="card card--dusk">
    <div class="card__scene" role="img" aria-label="Photograph of an airliner flying over a tropical shoreline with palm trees at dusk in deep blue tones"></div>
    <h2 class="card__name">employee name</h2>
    <p class="card__title">employee title</p>
    <div class="card__bar"></div>
    <address class="card__details">Tarvoe Aviation Consultants<br>End of Life Specialists<br>Dean Kross - President<br>418 SW 27th Ave<br>Fort Lauderdale, FL 33894<br>+1 954 555-0173</address>
  </article>

  <article class="card card--coral">
    <div class="card__scene" role="img" aria-label="Photograph of an airliner flying over a tropical shoreline with palm trees at a coral pink sunset"></div>
    <h2 class="card__name">employee name</h2>
    <p class="card__title">employee title</p>
    <address class="card__details">Tarvoe Aviation Consultants<br>End of Life Specialists<br>Dean Kross - President<br>418 SW 27th Ave<br>Fort Lauderdale, FL 33894<br>+1 954 555-0173</address>
  </article>

</main>
</body>
</html>
```